I need a business card that is professional /minimalistic ( clean edges) to help develop my new business venture that is car valeting / detailing.

I would like to use a black background, white font,red car silhouette above the text.

have now added phone numbers thanks

Industry/Entity Type

Business

Contact Information for Business Card

Gleamcraft Studio,
Valeting & Detailing Specialist,
tel 01638 219054 mob 07814 605193, Dean Marlowe, 7 Hawthorn Rise. East Brackley, Halsworth. IP19 3JD

```html
<!DOCTYPE html>
<html lang="en">
<head>
<meta charset="utf-8">
<title>Gleamcraft Studio – Business Card</title>
<link href="https://fonts.googleapis.com/css2?family=Questrial&display=swap" rel="stylesheet">
<style>
  :root {
    --page: #ffffff;
    --card: #000000;
    --card-edge: #2a2a2a;
    --band: #1b1b1b;
    --ink: #ffffff;
    --accent: #e0141b;
  }
  * { margin: 0; padding: 0; box-sizing: border-box; }
  html, body {
    width: 1200px;
    height: 791px;
    overflow: hidden;
    background: var(--page);
  }
  .card {
    position: absolute;
    left: 21px;
    top: 21px;
    width: 1157px;
    height: 749px;
    background: var(--card);
    border: 2px solid var(--card-edge);
    font-family: "Questrial", "Century Gothic", sans-serif;
    color: var(--ink);
  }
  .emblem {
    position: absolute;
    left: 288px;
    top: 208px;
    width: 530px;
    height: 99px;
    background: linear-gradient(90deg, rgba(224,20,27,0.15) 0%, var(--accent) 35%, var(--accent) 65%, rgba(224,20,27,0.15) 100%);
    border-radius: 50px 70px 10px 10px;
  }
  .headline {
    position: absolute;
    left: 0;
    right: 0;
    top: 364px;
    text-align: center;
    font-size: 45px;
    letter-spacing: 0.2px;
    font-weight: 400;
    white-space: nowrap;
  }
  .contact-band {
    position: absolute;
    left: 0;
    right: 0;
    bottom: 0;
    height: 170px;
    background: var(--band);
  }
  .phones {
    position: absolute;
    left: 202px;
    top: 21px;
    list-style: none;
  }
  .phones li {
    display: flex;
    align-items: center;
    height: 50px;
    font-size: 31px;
    white-space: nowrap;
  }
  .phones svg {
    width: 34px;
    height: 30px;
    margin-right: 33px;
    fill: var(--ink);
  }
  .divider {
    position: absolute;
    left: 540px;
    top: 32px;
    width: 4px;
    height: 94px;
    background: var(--ink);
  }
  .address {
    position: absolute;
    left: 595px;
    top: 22px;
    font-style: normal;
    font-size: 25px;
    line-height: 34px;
    white-space: nowrap;
  }
</style>
</head>
<body>
  <main class="card">
    <div class="emblem" role="img" aria-label="Red sports car silhouette in side profile"></div>

    <h1 class="headline">Gleamcraft Studio, Valeting &amp; Detailing Specialist</h1>

    <footer class="contact-band">
      <ul class="phones">
        <li>
          <svg viewBox="0 0 34 30" aria-label="Telephone">
            <path d="M2 10 C2 4 32 4 32 10 L32 13 L24 13 L24 9 C20 7.5 14 7.5 10 9 L10 13 L2 13 Z"/>
            <path d="M11 12 L23 12 L30 24 L30 28 L4 28 L4 24 Z"/>
            <circle cx="17" cy="20" r="4" fill="#1b1b1b"/>
          </svg>
          01638 219054
        </li>
        <li>
          <svg viewBox="0 0 34 30" aria-label="Mobile">
            <rect x="10" y="0" width="15" height="30" rx="3"/>
            <rect x="12.5" y="4" width="10" height="17" fill="#1b1b1b"/>
            <circle cx="17.5" cy="25" r="1.8" fill="#1b1b1b"/>
          </svg>
          07814 605193
        </li>
      </ul>
      <div class="divider"></div>
      <address class="address">
        Dean Marlowe, 7 Hawthorn Rise.<br>
        East Brackley, Halsworth.<br>
        IP19 3JD
      </address>
    </footer>
  </main>
</body>
</html>
```